Relocation/furniture installation company needs new business cards

we are a relocation and furniture installation company mainly dealing with corporate clients and we are looking for new business card ideas. Cards should incorporate our logo and list our website, phone number and services. The company is only 2 years old but with more staff joining we are in the need for more business cards, so something with an awesome design that is eye catching would go a long way to insure we get our name out there and look good to potential new clients.

Target Market(s)

Corporate

Industry/Entity Type

Trade

Contact Information for Business Card

www.merovanta.co.nz
0508 7 kelpor

furniture installation
business relocations
joinery installation
commercial property maintenance

Colors
0592cd
34a7d8
85cae6
85acd3
0356a4
cfdfed
cee9f5
757575
474747

Requirements
Must have
• Business relocations and furniture installation specialists
Nice to have
• something that incorporates our logo.

```html
<!DOCTYPE html>
<html lang="en">
<head>
<meta charset="utf-8">
<title>Merovanta Business Cards</title>
<link rel="stylesheet" href="https://fonts.googleapis.com/css2?family=Michroma&display=swap">
<style>
  :root {
    --page-bg: #e9edf1;
    --card-white: #ffffff;
    --brand-navy: #26349a;
    --band-top: #1f6cb6;
    --band-bottom: #0a9de2;
    --band-text: #ffffff;
    --mark-blue: #34a7d8;
  }
  * { margin: 0; padding: 0; box-sizing: border-box; }
  html, body {
    width: 1200px;
    height: 900px;
    overflow: hidden;
  }
  body {
    background: var(--page-bg);
    position: relative;
    font-family: "Michroma", sans-serif;
  }
  .card {
    position: absolute;
    background: var(--card-white);
    display: flex;
    flex-direction: column;
    box-shadow: 0 6px 18px rgba(0, 0, 0, 0.12);
  }
  .card--front { left: 177px; top: 73px; width: 590px; height: 365px; }
  .card--back  { left: 388px; top: 507px; width: 567px; height: 350px; }

  .card__brand {
    display: flex;
    align-items: center;
    justify-content: center;
    gap: 18px;
  }
  .card--front .card__brand { height: 205px; }
  .card--back .card__brand  { height: 167px; }

  .brand-square {
    background: var(--mark-blue);
    flex: none;
  }
  .brand-name {
    color: var(--brand-navy);
    letter-spacing: 2px;
    line-height: 1;
  }
  .card--front .brand-square { width: 40px; height: 40px; }
  .card--front .brand-name   { font-size: 38px; }
  .card--back .brand-square  { width: 36px; height: 36px; }
  .card--back .brand-name    { font-size: 35px; }

  .card__band {
    flex: 1;
    background: linear-gradient(to bottom, var(--band-top), var(--band-bottom));
    color: var(--band-text);
    display: flex;
    flex-direction: column;
    align-items: center;
    justify-content: center;
    text-align: center;
  }
  .contact-line {
    font-size: 21px;
    letter-spacing: 1.5px;
    line-height: 40px;
  }

  .service-list { list-style: none; }
  .service-item {
    font-size: 14px;
    letter-spacing: 1px;
    line-height: 34px;
    text-transform: uppercase;
  }
</style>
</head>
<body>
  <section class="card card--front">
    <header class="card__brand">
      <span class="brand-square"></span>
      <span class="brand-name">MEROVANTA</span>
    </header>
    <div class="card__band">
      <p class="contact-line contact-line--phone">0508 7 KELPOR</p>
      <p class="contact-line contact-line--url">WWW.MEROVANTA.CO.NZ</p>
    </div>
  </section>

  <section class="card card--back">
    <header class="card__brand">
      <span class="brand-square"></span>
      <span class="brand-name">MEROVANTA</span>
    </header>
    <div class="card__band">
      <ul class="service-list">
        <li class="service-item">Furniture Installation</li>
        <li class="service-item">Business Relocations</li>
        <li class="service-item">Joinery Installation</li>
        <li class="service-item">Commercial Property Maintenance</li>
      </ul>
    </div>
  </section>
</body>
</html>
```